Business Card Design Project

I am opening a skin care studio called Glow Haven by Marisol. I will be offering a wide range of unique and affordable skin services including facials, chemical peels, microdermabrasion treatments, body wraps, salt glows, all waxing and eye lash extensions. If the business cards depicts what I would like, this would lead to brochures, web design, signs, etc.
Updates

Project Deadline Extended
Reason: A request to extend deadline was requested. I will be more than happy to accommodate.

Industry/Entity Type

Business

Requirements
Nice to have
• facial features so prospective client clearly identifies what type of business this is. Not stuffy or boring "spa" looking graphics. I am focusing just on face, body, waxing, eyelashes. No massage or nails.

```html
<!DOCTYPE html>
<html lang="en">
<head>
<meta charset="utf-8">
<title>Glow Haven by Marisol – Business Card</title>
<link rel="stylesheet" href="https://fonts.googleapis.com/css2?family=Ubuntu:wght@400;500&display=swap">
<style>
  :root {
    --page-bg: #ffffff;
    --teal-light: #7ccaca;
    --teal-mid: #3fb0c2;
    --teal-deep: #1393b6;
    --brand-teal: #3aa9bb;
    --ink: #1e1e1e;
    --white: #ffffff;
    --photo-skin: #f1ddd3;
    --photo-leaf: #cfe6a8;
  }
  * { margin: 0; padding: 0; box-sizing: border-box; }
  html, body {
    width: 1069px; height: 1200px; overflow: hidden;
    background: var(--page-bg);
    font-family: "Ubuntu", "Trebuchet MS", sans-serif;
  }
  .canvas { position: relative; width: 1069px; height: 1200px; }

  .card {
    position: absolute; left: 118px; width: 835px; height: 510px;
    border-radius: 26px; overflow: hidden;
  }

  /* Front */
  .card--front {
    top: 55px;
    background: radial-gradient(ellipse 75% 85% at 42% 28%, var(--teal-light) 0%, var(--teal-mid) 50%, var(--teal-deep) 100%);
    color: var(--white);
  }
  .card--front .brand-name {
    position: absolute; top: 222px; left: 0; width: 100%;
    text-align: center; font-size: 58px; font-weight: 500; letter-spacing: -0.5px;
  }
  .card--front .web {
    position: absolute; top: 444px; left: 0; width: 100%;
    text-align: center; font-size: 24px; letter-spacing: 0.3px;
  }

  /* Back */
  .card--back {
    top: 612px; background: var(--white);
    box-shadow: 0 2px 10px rgba(0,0,0,0.22);
  }
  .card__photo {
    position: absolute; left: 0; top: 0; width: 470px; height: 100%;
    background:
      radial-gradient(ellipse 40% 45% at 36% 42%, var(--photo-skin) 0%, rgba(241,221,211,0) 100%),
      radial-gradient(ellipse 25% 40% at 62% 80%, var(--photo-leaf) 0%, rgba(207,230,168,0) 100%),
      linear-gradient(90deg, #e9e3df 0%, rgba(255,255,255,0) 100%);
  }
  .card--back .brand-name {
    position: absolute; top: 124px; left: 384px;
    font-size: 46px; font-weight: 500; color: var(--brand-teal); letter-spacing: -0.5px;
  }
  .contact {
    position: absolute; top: 334px; left: 308px;
    display: grid; grid-template-columns: 120px 22px auto;
    row-gap: 2px; font-size: 22px; line-height: 28px; color: var(--ink);
  }
  .contact dt { grid-column: 1; }
  .contact dd { grid-column: 3; }
  .contact .sep { grid-column: 2; }
</style>
</head>
<body>
<main class="canvas">
  <section class="card card--front">
    <h1 class="brand-name">Glow Haven by Marisol</h1>
    <p class="web">www.glowhavenbymarisol.com</p>
  </section>

  <section class="card card--back">
    <div class="card__photo" role="img" aria-label="Photo of a smiling woman applying cream to her cheek beside fresh green leaves, fading into white"></div>
    <h2 class="brand-name">Glow Haven by Marisol</h2>
    <dl class="contact">
      <dt>Address</dt><span class="sep">:</span><dd>412 Cedar Avenue Lakewood,<br>CO 80214</dd>
      <dt>Phone</dt><span class="sep">:</span><dd>970-555-0142</dd>
      <dt>Facebook</dt><span class="sep">:</span><dd>glowhavenbymarisol</dd>
      <dt>Website</dt><span class="sep">:</span><dd>www.glowhavenbymarisol.com</dd>
    </dl>
  </section>
</main>
</body>
</html>
```